Business Card Design Project

I need business cards communicate a high end look and cutting edge sophistication,creativity, with a logo branding.
The company name is: Keystone Crafters we specialize in Remodel ing and Design of Resindental and Commercial our company is based in Los Angeles Ca our clients are high end high dollar . The design should communicate the statements above.
Updates
I would like to see both side the business card
Industry/Entity Type
Business
Requirements
Nice to have
- Maybe a design with a faint Blueprint /construction floor plan background, maybe

```html
<!DOCTYPE html>
<html lang="en">
<head>
<meta charset="utf-8">
<title>Keystone Crafters Business Card</title>
<link href="https://fonts.googleapis.com/css2?family=Tenor+Sans&display=swap" rel="stylesheet">
<style>
  :root {
    --strip-light: #d5d6d8;
    --strip-mid: #a9aaad;
    --navy: #183f66;
    --navy-soft: #26507a;
    --white: #ffffff;
  }
  html, body {
    margin: 0;
    padding: 0;
    width: 1200px;
    height: 686px;
    overflow: hidden;
    background: var(--white);
  }
  .card {
    position: relative;
    width: 1200px;
    height: 686px;
    overflow: hidden;
    font-family: "Tenor Sans", sans-serif;
    font-variant: small-caps;
  }
  .edge-strip {
    position: absolute;
    top: 0; left: 0;
    width: 69px; height: 686px;
    background: var(--strip-light);
  }
  .name-strip {
    position: absolute;
    top: 0; left: 69px;
    width: 123px; height: 686px;
    background: var(--strip-mid);
  }
  .person-name {
    position: absolute;
    left: 131px;
    top: 342px;
    transform: translate(-50%, -50%) rotate(-90deg);
    white-space: nowrap;
    color: var(--navy);
    font-size: 36px;
    letter-spacing: 5px;
    margin: 0;
  }
  .brand-panel {
    position: absolute;
    top: 0; left: 192px;
    width: 1008px; height: 686px;
    background: var(--navy);
  }
  .house-elevation {
    position: absolute;
    left: 217px; top: 92px;
    width: 983px; height: 594px;
    background: radial-gradient(ellipse at 50% 45%, var(--navy-soft) 0%, var(--navy) 75%);
  }
  .roofline {
    position: absolute;
    top: 0; left: 0;
  }
  .company-name {
    position: absolute;
    left: 283px;
    top: 92px;
    margin: 0;
    color: var(--white);
    font-size: 56px;
    font-weight: 400;
    letter-spacing: 5px;
    line-height: 1;
    white-space: nowrap;
  }
  .contact {
    position: absolute;
    left: 283px;
    top: 364px;
    margin: 0;
    color: var(--white);
    font-size: 32px;
    letter-spacing: 3px;
    font-style: normal;
    line-height: 49px;
    white-space: nowrap;
  }
  .contact .email {
    margin-top: 49px;
    display: block;
  }
</style>
</head>
<body>
  <div class="card">
    <div class="edge-strip"></div>
    <div class="name-strip"></div>
    <p class="person-name">Marcus Ellison</p>

    <div class="brand-panel"></div>
    <div class="house-elevation" role="img" aria-label="Faint blueprint elevation drawing of a two-storey house"></div>

    <svg class="roofline" width="1200" height="686" viewBox="0 0 1200 686" aria-hidden="true">
      <polygon points="221,74 692,32 1174,77 1174,92 692,48 221,89" fill="var(--white)"/>
    </svg>

    <h1 class="company-name">Keystone Crafters</h1>

    <address class="contact">
      <span>Phone: (323) 555-0147</span><br>
      <span>4820 Larchmont Ave Ste. #900</span><br>
      <span>Los Angeles, CA 90004</span>
      <span class="email">Email: marcus@keystonecrafters.net</span>
    </address>
  </div>
</body>
</html>
```